Brevard's Jewelers Big Sale

Brevard's Jewelers is an independent fine store in Fort Worth, Texas. We have been in business since 1893 and we only have one sale per year. This is our 120th year. Our stores are upscale and our one sale is similar to a Corwin Ashby Final Bell.

we need to include:
up to 60% off
diamonds, watches, fashion designer jewelry and gifts
sale dates April 4th through April 13th
all sales are final
*we are sorry, but Vantor and Lumisse are not included.

Reason: We like some of the designs, but we are still looking for a great headline or name for the sale. thanks!

Requirements
Must have
• must show our logo, which is in the uploaded file.

we also need to list our stores:
Downtown, Elm and 7th St. 555-214-7730
4817 Larkspur Ridge Blvd, 555-691-2048
Willowmere Commons, 555-832-5196
Bramblecrest Village Plaza, 555-407-9361
Nice to have
• We would like a catchy tag line that will look good in color print, black and white newspaper and billboard.
Should not have
• We do not want a high impact, low-end sale look.

```html
<!DOCTYPE html>
<html lang="en">
<head>
<meta charset="utf-8">
<title>Brevard's Jewelers – Best Shoping Days Back Again</title>
<link rel="stylesheet" href="https://fonts.googleapis.com/css2?family=Source+Sans+3:wght@400;600;700&family=Libre+Caslon+Text:wght@700&display=swap">
<style>
  :root {
    --green: #124d29;
    --cream: #efe6c2;
    --cream-light: #f4edcf;
    --white: #ffffff;
    --ink: #111111;
  }
  * { margin: 0; padding: 0; box-sizing: border-box; }
  html, body { width: 928px; height: 1200px; overflow: hidden; }
  body {
    position: relative;
    font-family: "Source Sans 3", "Myriad Pro", sans-serif;
    background: radial-gradient(ellipse at 50% 40%, var(--cream-light), var(--cream) 75%);
    color: var(--ink);
  }
  .headline-panel {
    position: absolute; left: 29px; top: 46px; width: 878px; height: 244px;
    background: var(--white);
    border: 1px solid #e2ddd0;
  }
  .headline {
    position: absolute; left: 24px; top: 40px;
    font-size: 72px; font-weight: 400; line-height: 92px; letter-spacing: -0.5px;
  }
  .discount-badge {
    position: absolute; left: 652px; top: 17px; width: 209px; height: 208px;
    background: var(--green); color: var(--white);
    padding: 12px 0 0 12px;
  }
  .discount-badge .upto { font-size: 26px; font-weight: 600; letter-spacing: 1px; line-height: 30px; }
  .discount-badge .percent { font-size: 72px; font-weight: 700; line-height: 66px; margin-top: 6px; }
  .discount-badge .off { font-size: 90px; font-weight: 700; line-height: 80px; letter-spacing: -1px; }
  .sale-dates {
    position: absolute; right: 58px; top: 310px;
    font-size: 27px; font-weight: 700;
  }
  .category-list { list-style: none; position: absolute; left: 0; top: 478px; }
  .category-list li {
    position: relative; height: 53px; margin-bottom: 11px;
    padding-left: 79px;
    font-size: 32px; color: var(--green); line-height: 50px;
  }
  .category-list li::before {
    content: ""; position: absolute; left: 0; top: 0; width: 68px; height: 53px;
    background: var(--white);
    border-radius: 0 0 0 0;
    clip-path: polygon(0 0, 88% 0, 80% 8%, 80% 92%, 88% 100%, 0 100%);
  }
  .fine-print {
    position: absolute; left: 83px; top: 874px;
    font-size: 20px; line-height: 27px;
  }
  .store-band {
    position: absolute; left: 0; top: 933px; width: 928px; height: 267px;
    background: var(--green);
  }
  .store-list {
    position: absolute; right: 368px; top: 96px;
    list-style: none; text-align: right; color: var(--white);
    font-size: 18.5px; line-height: 23.7px;
  }
  .brand-panel {
    position: absolute; left: 573px; top: 73px; width: 355px; height: 136px;
    background: var(--white);
    display: flex; align-items: center; justify-content: center; gap: 12px;
  }
  .brand-mark { width: 14px; height: 14px; background: var(--ink); }
  .brand-name {
    font-family: "Libre Caslon Text", serif; font-weight: 700;
    font-size: 30px; color: var(--ink); letter-spacing: -0.5px;
  }
</style>
</head>
<body>
  <section class="headline-panel">
    <h1 class="headline">Best Shoping Days<br>Back Again</h1>
    <div class="discount-badge">
      <div class="upto">UPTO</div>
      <div class="percent">60 %</div>
      <div class="off">OFF</div>
    </div>
  </section>

  <p class="sale-dates">April 4 to 13</p>

  <ul class="category-list">
    <li>diamonds</li>
    <li>watches</li>
    <li>fashion designer jewelry</li>
    <li>gifts</li>
  </ul>

  <p class="fine-print">all sales are final<br>*we are sorry, but Vantor and Lumisse are not included.</p>

  <footer class="store-band">
    <ul class="store-list">
      <li>Downtown, Elm and 7th St. 555-214-7730</li>
      <li>4817 Larkspur Ridge Blvd, 555-691-2048</li>
      <li>Willowmere Commons, 555-832-5196</li>
      <li>Bramblecrest Village Plaza, 555-407-9361</li>
    </ul>
    <div class="brand-panel">
      <span class="brand-mark"></span>
      <span class="brand-name">Brevard's Jewelers</span>
    </div>
  </footer>
</body>
</html>
```